Blue Mesa Fuels-Ethanol Plant-Business Card Design

We are looking to incorporate a new logo on a new business card design. Can be vertical or horizontal.
We currently produce a variety of feed products as well as pharmaceutical grade ethanol that can be used in hand sanitizers, medications, and vaccines and hospitals for sterilization. We are also the first company to incorporate Carbon Capture and Storage (CCS) which takes all of our CO2 emissions and injects it deep into the earth-about 6400 feet below our facility.
For our logo we are looking for something professional, detailed, yet simple looking that can be used for all areas of our company. Something 'timeless' that can be used for many years to come, no matter what future projects our company takes on.
Industry/Entity Type
Corn/Ethanol Plant
Contact Information for Business Card
First & Last Name, Title, E-Mail, Office Phone: 555.210.4471 Ext. 1000 , Fax: 555.210.4472, Cell: 555.386.9025, Email: Info@bluemesafuels.example, Address: 5149 Route 4 N PO Box 27 Alderton, ND 50917, Website: www.bluemesafuels.example
Look and feel

```html
<!DOCTYPE html>
<html lang="en">
<head>
<meta charset="utf-8">
<title>Blue Mesa Fuels – Business Card Options</title>
<link href="https://fonts.googleapis.com/css2?family=Arimo:wght@400;700&display=swap" rel="stylesheet">
<style>
  :root {
    --backdrop: #d6d6f4;
    --accent: #ec3237;
    --ink: #3a3c42;
    --ink-dark-card: #4a4d55;
    --paper: #ffffff;
    --night: #000000;
    --label: #000000;
  }
  * { margin: 0; padding: 0; box-sizing: border-box; }
  html, body { width: 1200px; height: 1200px; overflow: hidden; }
  body {
    background: var(--backdrop);
    font-family: "Arimo", Arial, sans-serif;
    position: relative;
  }
  .option-label {
    position: absolute;
    top: 270px;
    width: 120px;
    text-align: center;
    font-size: 58px;
    font-weight: 400;
    color: var(--label);
  }
  .label-a { left: 252px; }
  .label-b { left: 828px; }

  .card {
    position: absolute;
    width: 472px;
    height: 270px;
    overflow: hidden;
  }
  .card-light { background: var(--paper); }
  .card-dark { background: var(--night); }
  .col-a { left: 75px; }
  .col-b { left: 653px; }
  .row-front { top: 352px; }
  .row-back { top: 648px; }

  /* Brand name block */
  .brand {
    position: absolute;
    display: flex;
    align-items: center;
    gap: 10px;
    font-weight: 700;
    color: var(--ink);
    white-space: nowrap;
    letter-spacing: 0.5px;
  }
  .card-dark .brand { color: var(--ink-dark-card); }
  .brand-mark { background: var(--accent); flex: none; }
  .front .brand {
    left: 0; right: 0; top: 112px;
    justify-content: center;
    font-size: 32px;
  }
  .front .brand-mark { width: 26px; height: 26px; }
  .back .brand {
    left: 0; width: 230px; top: 124px;
    justify-content: center;
    font-size: 19px;
  }
  .back .brand-mark { width: 16px; height: 16px; }

  .stripe { position: absolute; left: 0; top: 238px; width: 472px; height: 13px; }
  .front-web {
    position: absolute;
    right: 6px; top: 255px;
    font-size: 12px;
    color: var(--paper);
  }

  /* Contact side */
  .rule-main {
    position: absolute; left: 229px; top: 20px;
    width: 3px; height: 230px; background: var(--accent);
  }
  .rule-inner {
    position: absolute; left: 225px; top: 62px;
    width: 2px; height: 146px; background: var(--accent);
  }
  .card-dark .rule-inner { background: var(--paper); }

  .contact { position: absolute; left: 0; top: 0; width: 100%; height: 100%; }
  .contact-row {
    position: absolute;
    left: 250px;
    display: flex;
    align-items: flex-start;
    gap: 10px;
    font-size: 12px;
    line-height: 15px;
    color: var(--accent);
  }
  .card-dark .contact-row { color: var(--paper); }
  .contact-row svg { width: 14px; height: 14px; fill: var(--accent); flex: none; margin-top: 1px; }
  .person-name { font-size: 17.5px; line-height: 18px; letter-spacing: 0.2px; }
  .person-title { font-size: 10.5px; line-height: 12px; }
  .person { display: flex; flex-direction: column; }
</style>
</head>
<body>

<svg width="0" height="0" style="position:absolute" aria-hidden="true">
  <defs>
    <symbol id="icon-person" viewBox="0 0 16 16"><circle cx="8" cy="5" r="3.4"/><path d="M1.5 15c0-3.6 2.9-5.6 6.5-5.6s6.5 2 6.5 5.6z"/></symbol>
    <symbol id="icon-desk-phone" viewBox="0 0 16 16"><path d="M1 6c0-2 3-3.2 7-3.2S15 4 15 6v1.3h-3.2V5.6H4.2v1.7H1z"/><rect x="2" y="8" width="12" height="6.5" rx="1.5"/></symbol>
    <symbol id="icon-mobile" viewBox="0 0 16 16"><path d="M4 1.2l2.4 3-1.4 1.6c.9 2 2.3 3.4 4.3 4.3l1.6-1.4 3 2.4-1.6 2.7C7.5 13.6 2.4 8.5 1.2 3z"/></symbol>
    <symbol id="icon-fax" viewBox="0 0 16 16"><rect x="4" y="1.5" width="8" height="4"/><rect x="1" y="5.5" width="14" height="6.5" rx="1.2"/><rect x="4" y="10" width="8" height="4.5"/></symbol>
    <symbol id="icon-pin" viewBox="0 0 16 16"><path d="M8 1a5 5 0 0 0-5 5c0 3.7 5 9 5 9s5-5.3 5-9a5 5 0 0 0-5-5zm0 7.2A2.2 2.2 0 1 1 8 3.8a2.2 2.2 0 0 1 0 4.4z"/></symbol>
    <symbol id="icon-mail" viewBox="0 0 16 16"><path d="M0.5 3h15v10h-15zM2 4.3v.4l6 4.3 6-4.3v-.4zm0 2.2v5.2l3.4-2.8zm12 0l-3.4 2.4 3.4 2.8z"/></symbol>
    <symbol id="icon-globe" viewBox="0 0 16 16"><path d="M8 1.5a6.5 6.5 0 1 0 0 13 6.5 6.5 0 0 0 0-13zm0 1.4c.8.9 1.4 2.3 1.6 4.1H6.4C6.6 5.2 7.2 3.8 8 2.9zM3 7h2.2c.1-1.5.5-2.8 1-3.7A5.1 5.1 0 0 0 3 7zm7.8 0H13a5.1 5.1 0 0 0-3.2-3.7c.5.9.9 2.2 1 3.7zM3 9a5.1 5.1 0 0 0 3.2 3.7c-.5-.9-.9-2.2-1-3.7zm3.4 0c.2 1.8.8 3.2 1.6 4.1.8-.9 1.4-2.3 1.6-4.1zm4.4 0c-.1 1.5-.5 2.8-1 3.7A5.1 5.1 0 0 0 13 9z"/></symbol>
    <symbol id="split-stripe" viewBox="0 0 472 13"><polygon fill="#ec3237" points="0,0 98,0 86,13 0,13"/><polygon fill="#ec3237" points="120,0 472,0 472,13 106,13"/></symbol>
  </defs>
</svg>

<div class="option-label label-a">A</div>
<div class="option-label label-b">B</div>

<!-- Option A front -->
<section class="card card-light front col-a row-front">
  <div class="brand"><span class="brand-mark"></span>BLUE MESA FUELS</div>
  <svg class="stripe" viewBox="0 0 472 13"><use href="#split-stripe"/></svg>
</section>

<!-- Option B front -->
<section class="card card-dark front col-b row-front">
  <div class="brand"><span class="brand-mark"></span>BLUE MESA FUELS</div>
  <svg class="stripe" viewBox="0 0 472 13"><use href="#split-stripe"/></svg>
  <div class="front-web">www.bluemesafuels.example</div>
</section>

<!-- Option A back -->
<section class="card card-light back col-a row-back">
  <div class="brand"><span class="brand-mark"></span>BLUE MESA FUELS</div>
  <div class="rule-main"></div>
  <div class="rule-inner"></div>
  <div class="contact">
    <div class="contact-row" style="top:27px"><svg style="margin-top:10px"><use href="#icon-person"/></svg><div class="person"><span class="person-name">HAROLD VENNSTROM</span><span class="person-title">Chief Executive Officer</span></div></div>
    <div class="contact-row" style="top:71px"><svg><use href="#icon-desk-phone"/></svg>555.210.4471 Ext. 1000</div>
    <div class="contact-row" style="top:102px"><svg><use href="#icon-mobile"/></svg>555.386.9025</div>
    <div class="contact-row" style="top:133px"><svg><use href="#icon-fax"/></svg>555.210.4472</div>
    <div class="contact-row" style="top:164px"><svg><use href="#icon-pin"/></svg><span>5149 Route 4 N PO Box 27 Alderton<br>ND 50917</span></div>
    <div class="contact-row" style="top:200px"><svg><use href="#icon-mail"/></svg>Info@bluemesafuels.example</div>
    <div class="contact-row" style="top:229px"><svg><use href="#icon-globe"/></svg>www.bluemesafuels.example</div>
  </div>
</section>

<!-- Option B back -->
<section class="card card-dark back col-b row-back">
  <div class="brand"><span class="brand-mark"></span>BLUE MESA FUELS</div>
  <div class="rule-main"></div>
  <div class="rule-inner"></div>
  <div class="contact">
    <div class="contact-row" style="top:27px"><svg style="margin-top:10px"><use href="#icon-person"/></svg><div class="person"><span class="person-name">HAROLD VENNSTROM</span><span class="person-title">Chief Executive Officer</span></div></div>
    <div class="contact-row" style="top:71px"><svg><use href="#icon-desk-phone"/></svg>555.210.4471 Ext. 1000</div>
    <div class="contact-row" style="top:102px"><svg><use href="#icon-mobile"/></svg>555.386.9025</div>
    <div class="contact-row" style="top:133px"><svg><use href="#icon-fax"/></svg>555.210.4472</div>
    <div class="contact-row" style="top:164px"><svg><use href="#icon-pin"/></svg><span>5149 Route 4 N PO Box 27 Alderton<br>ND 50917</span></div>
    <div class="contact-row" style="top:200px"><svg><use href="#icon-mail"/></svg>Info@bluemesafuels.example</div>
    <div class="contact-row" style="top:229px"><svg><use href="#icon-globe"/></svg>www.bluemesafuels.example</div>
  </div>
</section>

</body>
</html>
```